Business Card Design for Vel
Fun, earthy, organic food company needs professional cards to speak our message!
Business Card Design for Vel -
Creative Brief
Bright & Fun-filled
Marcus Dell
Managing Member & Co-Founder
PO Box 482937 Dallas, TX 75318-2937
mdell@ourvelway.com
http:\\www.ourvelway.com
If you can access the closed project, we'll be using logo #84 in the folowing link: http://www.kavdrafthub.com/contests/logo-for-vel. We'll be uploading the logo file shortly for this project. We like simple, fun and creative but are open to many designs and styles.
The back of the card should be our logo colors, green and brown. It could be a cool design based off of the colors, you could use the entire length of the back with the logo or place both colors on the back with it being split with a similar design of the tree in our logo. We're open to your creativity!
quelldraw quelldraw
@KR - working on it now & submit our conmcepts soon! Thanks
Fovra Fovra
Please Check top right message box of the page.
trolen447 trolen447
Designers, We're looking to expedite the process on this. First come first serve on the card design. If you provide designs for stationary as well and we choose you, we'll provide a $50 donation to you. We're even open to selecting two winners for business card and stationary. So submit for each, because you could win for either or both! Thanks!

```html
<!DOCTYPE html>
<html lang="en">
<head>
<meta charset="utf-8">
<title>Vel – Business Card</title>
<link href="https://fonts.googleapis.com/css2?family=Source+Sans+3:wght@400;600;700&display=swap" rel="stylesheet">
<style>
  :root {
    --leaf-green: #7dc242;
    --bark-brown: #4a2a12;
    --card-white: #ffffff;
    --ink: #3b3b3b;
    --rule: #c9c9c9;
    --backdrop: #e9e6e1;
  }
  html, body {
    margin: 0;
    padding: 0;
    width: 1200px;
    height: 780px;
    overflow: hidden;
    background: var(--backdrop);
    font-family: "Source Sans 3", "Myriad Pro", Arial, sans-serif;
  }
  .canvas {
    position: relative;
    width: 1200px;
    height: 780px;
  }
  .card {
    position: absolute;
    left: 100px;
    top: 104px;
    width: 1000px;
    height: 572px;
    background: var(--card-white);
    border-radius: 34px;
    overflow: hidden;
    box-shadow: 0 10px 28px rgba(0,0,0,0.18);
  }
  .card-band {
    position: absolute;
    inset: 0;
    width: 1000px;
    height: 572px;
  }
  .band-green { fill: var(--leaf-green); }
  .band-brown { fill: var(--bark-brown); }

  .holder {
    position: absolute;
    right: 48px;
    top: 30px;
    text-align: right;
    color: var(--card-white);
  }
  .holder-name {
    margin: 0;
    font-size: 40px;
    font-weight: 700;
    line-height: 1.1;
  }
  .holder-title {
    margin: 6px 0 0;
    font-size: 25px;
    font-weight: 400;
    line-height: 1.2;
  }

  .brand {
    position: absolute;
    left: 92px;
    top: 262px;
    display: flex;
    align-items: center;
    gap: 22px;
  }
  .brand-square {
    width: 64px;
    height: 64px;
    background: var(--leaf-green);
  }
  .brand-name {
    font-size: 104px;
    font-weight: 700;
    color: var(--bark-brown);
    line-height: 1;
  }

  .divider {
    position: absolute;
    left: 430px;
    top: 220px;
    width: 2px;
    height: 280px;
    background: linear-gradient(to bottom, rgba(201,201,201,0), var(--rule) 30%, var(--rule) 70%, rgba(201,201,201,0));
  }

  .address {
    position: absolute;
    left: 478px;
    top: 232px;
    margin: 0;
    font-size: 26px;
    line-height: 1.3;
    color: var(--ink);
    font-style: normal;
  }
  .contacts {
    position: absolute;
    left: 478px;
    top: 356px;
    margin: 0;
    padding: 0;
    list-style: none;
    font-size: 25px;
    color: var(--ink);
  }
  .contact {
    display: flex;
    align-items: center;
    gap: 14px;
    height: 40px;
  }
  .contact-icon {
    width: 22px;
    height: 22px;
    fill: var(--leaf-green);
    flex: none;
  }
</style>
</head>
<body>
<main class="canvas">
  <article class="card">
    <svg class="card-band" viewBox="0 0 1000 572" aria-hidden="true">
      <path class="band-green" d="M0 0 H1000 V190 C820 200 560 150 360 150 C200 150 80 170 0 200 Z"/>
      <path class="band-brown" d="M0 200 C80 170 200 150 360 150 C560 150 820 200 1000 190 C800 214 560 172 360 174 C210 176 90 200 0 236 Z"/>
    </svg>

    <header class="holder">
      <h1 class="holder-name">Marcus Dell</h1>
      <p class="holder-title">Managing Member &amp;<br>Co-Founder</p>
    </header>

    <div class="brand">
      <span class="brand-square"></span>
      <span class="brand-name">Vel</span>
    </div>

    <div class="divider"></div>

    <address class="address">PO Box 482937<br>Dallas, TX 75318-2937</address>

    <ul class="contacts">
      <li class="contact">
        <svg class="contact-icon" viewBox="0 0 24 24" aria-hidden="true"><path d="M6.6 10.8c1.4 2.8 3.8 5.1 6.6 6.6l2.2-2.2c.3-.3.7-.4 1-.2 1.1.4 2.3.6 3.6.6.6 0 1 .4 1 1V20c0 .6-.4 1-1 1C10.6 21 3 13.4 3 4c0-.6.4-1 1-1h3.5c.6 0 1 .4 1 1 0 1.3.2 2.5.6 3.6.1.3 0 .7-.2 1z"/></svg>
        <span>214-555-0147</span>
      </li>
      <li class="contact">
        <svg class="contact-icon" viewBox="0 0 24 24" aria-hidden="true"><path d="M2 5h20v14H2z M4 7v.5l8 5 8-5V7z" fill-rule="evenodd"/></svg>
        <span>mdell@ourvelway.com</span>
      </li>
      <li class="contact">
        <svg class="contact-icon" viewBox="0 0 24 24" aria-hidden="true"><circle cx="12" cy="12" r="10"/><path d="M2 12h20M12 2c3 3 3 17 0 20M12 2c-3 3-3 17 0 20" stroke="#fff" stroke-width="1.4" fill="none"/></svg>
        <span>www.ourvelway.com</span>
      </li>
    </ul>
  </article>
</main>
</body>
</html>
```